Business Card & Stationary Design Project

We are looking for some creative direction for business cards and our stationary.

We are a global logistics firm that has recently changed its name to Marwick Global Logistics and we have a new website due out tomorrow (www.marwick.com.au).

The colours of the company are rich navy tones, I would like to have business cards that fit together to make one picture on the back (possibly an old map of the world??), and the front to be modern contemporary looking.

But I am open to suggestions, so just incorporate our new logo and get going!
Updates

Hi Everyone,

Thank you for all of your designs so far and the time you have put into it.

I have asked many of you for amendments to see if we can get a final product, so with this in mind I am extending the deadline by a few days.

Good luck and thank you once again.

Please message me direct if you need any clarification.

Kind Regards
Tobias

Reason: As outlined the extra 3 days is for amendments and changes to the current submissions. Thanks Tobias

Industry/Entity Type

Business

```html
<!DOCTYPE html>
<html lang="en">
<head>
<meta charset="utf-8">
<title>Marwick Global Logistics – Stationery Suite</title>
<link rel="stylesheet" href="https://fonts.googleapis.com/css2?family=Open+Sans:wght@400;600&display=swap">
<style>
:root{
  --navy-deep:#1d3f7c;
  --navy:#24508f;
  --navy-glow:#4a8ccb;
  --ink:#2a3f7a;
  --body-grey:#8a8a8a;
  --rule:#d6d6d6;
  --map-tint:#e9e9e9;
  --paper:#ffffff;
  --backdrop:#e4e4e4;
}
*{margin:0;padding:0;box-sizing:border-box}
html,body{width:1200px;height:858px;overflow:hidden;background:var(--backdrop);font-family:"Open Sans",Arial,sans-serif}
.canvas{position:relative;width:1200px;height:858px}
.sheet{position:absolute;background:var(--paper);overflow:hidden}
.brand-name{font-family:"Open Sans",Arial,sans-serif;font-weight:400;text-transform:uppercase;color:var(--ink);line-height:1}
.brand-name .word{display:block;letter-spacing:.42em}
.brand-name .line2{display:block;letter-spacing:.5em;font-size:.38em;margin-top:.35em}
.brand-dot{position:absolute;border-radius:50%;background:var(--navy)}
.map-fade{position:absolute;border-radius:50%;background:radial-gradient(ellipse at center,var(--map-tint) 0%,rgba(233,233,233,.6) 45%,rgba(233,233,233,0) 72%)}

/* Presentation folder */
.folder{left:153px;top:78px;width:389px;height:549px;background:radial-gradient(ellipse 70% 55% at 50% 62%,var(--navy-glow) 0%,var(--navy) 55%,var(--navy-deep) 100%)}
.folder .brand-dot{left:184px;top:146px;width:30px;height:30px;background:#fff;opacity:.9}
.folder .brand-name{position:absolute;left:0;width:100%;top:200px;text-align:center;color:#fff;font-size:20px}
.folder .url{position:absolute;left:0;width:100%;top:242px;text-align:center;color:#fff;font-size:9.5px;letter-spacing:.1em}
.folder .map-fade{left:90px;top:290px;width:210px;height:220px;background:radial-gradient(ellipse at center,rgba(140,180,225,.28) 0%,rgba(140,180,225,0) 70%)}

/* Letterhead */
.letterhead{left:565px;top:78px;width:388px;height:549px}
.letterhead .brand-name{position:absolute;left:33px;top:40px;font-size:11px}
.letterhead .brand-dot{left:115px;top:28px;width:32px;height:32px}
.address{position:absolute;text-align:right;color:var(--ink);font-size:6.5px;line-height:8.6px}
.letterhead .address{right:30px;top:23px}
.contact-line{display:flex;align-items:center;justify-content:flex-end;gap:4px}
.icon{width:6px;height:6px;fill:var(--ink)}
.salutation{position:absolute;left:36px;top:121px;font-size:6.8px;color:var(--body-grey)}
.letter-body{position:absolute;left:36px;top:154px;width:316px;font-size:6.3px;line-height:10.8px;color:var(--body-grey);text-align:justify}
.letter-body p{margin-bottom:10.8px}
.signoff{position:absolute;left:41px;top:389px;font-size:5.6px;color:var(--body-grey)}
.signature{position:absolute;left:34px;top:399px;width:52px;height:14px;border-radius:7px;background:linear-gradient(90deg,#d2d2d2,#ececec)}
.sign-title{position:absolute;left:46px;top:415px;font-size:5.6px;color:var(--body-grey)}
.letterhead .map-fade{left:240px;top:385px;width:170px;height:160px}
.footer-url{position:absolute;font-size:7px;color:var(--ink)}
.letterhead .footer-url{left:28px;top:523px}

/* Business card – back */
.card-back{left:1002px;top:194px;width:159px;height:94px;background:radial-gradient(ellipse 80% 80% at 70% 50%,var(--navy-glow) 0%,var(--navy) 60%,var(--navy-deep) 100%)}
.card-back .brand-name{position:absolute;left:40px;top:43px;font-size:7px;color:#fff}
.card-back .brand-dot{left:110px;top:36px;width:20px;height:20px;background:#fff;opacity:.9}
.card-back .url{position:absolute;left:40px;top:58px;font-size:3.6px;color:#fff}

/* Business card – front */
.card-front{left:1000px;top:314px;width:163px;height:94px}
.card-front .brand-name{position:absolute;left:15px;top:18px;font-size:6.4px}
.card-front .brand-dot{left:75px;top:10px;width:19px;height:19px}
.person{position:absolute;left:15px;top:42px;color:var(--ink);font-size:4.4px;line-height:5.2px}
.person .role{font-size:3.6px;color:#666}
.card-front .address{left:15px;top:64px;text-align:left;font-size:3.4px;line-height:4.3px;color:#555}
.card-contacts{position:absolute;left:105px;top:45px;font-size:3.4px;line-height:5.2px;color:#555}
.card-contacts .contact-line{justify-content:flex-start;gap:3px}
.card-contacts .icon{width:3.6px;height:3.6px}

/* Compliment slip */
.slip{left:153px;top:650px;width:391px;height:171px}
.slip .brand-name{position:absolute;left:16px;top:25px;font-size:10px}
.slip .brand-dot{left:86px;top:13px;width:29px;height:29px}
.slip .address{left:16px;top:42px;text-align:left;font-size:6px;line-height:7px;color:#555}
.slip .map-fade{left:250px;top:25px;width:150px;height:150px}
.slip .footer-url{left:16px;top:153px}

/* Envelope */
.envelope{left:565px;top:652px;width:388px;height:171px}
.envelope svg.flap{position:absolute;left:0;top:0}
.envelope .brand-name{position:absolute;left:0;width:100%;top:16px;text-align:center;color:#fff;font-size:12px}

/* Note pad */
.notepad{left:1001px;top:617px;width:160px;height:198px}
.notepad .brand-name{position:absolute;left:13px;top:17px;font-size:6.4px}
.notepad .brand-dot{left:67px;top:10px;width:18px;height:18px}
.note-lines{position:absolute;left:11px;top:53px;width:137px}
.note-lines span{display:block;height:8.6px;border-bottom:1px solid var(--rule)}
.notepad .map-fade{left:70px;top:120px;width:100px;height:90px}
.notepad .address{left:11px;top:156px;text-align:left;font-size:3.4px;line-height:4.6px;color:#555}
.notepad .address .contact-line{justify-content:flex-start;gap:2px}
.notepad .address .icon{width:3.4px;height:3.4px}
.notepad .footer-url{left:11px;top:188px;font-size:3.6px}
</style>
</head>
<body>
<main class="canvas">

  <!-- Presentation folder -->
  <section class="sheet folder" aria-label="Presentation folder">
    <div class="map-fade" role="img" aria-label="Faint world map showing Asia and Australia"></div>
    <span class="brand-dot"></span>
    <div class="brand-name"><span class="word">Marwick</span><span class="line2">Global Logistics</span></div>
    <div class="url">www.marwick.com.au</div>
  </section>

  <!-- Letterhead -->
  <section class="sheet letterhead" aria-label="Letterhead">
    <div class="brand-name"><span class="word">Marwick</span><span class="line2">Global Logistics</span></div>
    <span class="brand-dot"></span>
    <div class="address">
      <div>58 Harbour Lane</div>
      <div>Pyrmont</div>
      <div>NSW 2009</div>
      <div class="contact-line"><svg class="icon" viewBox="0 0 10 10"><path d="M2 1l2 2-1 1.5c.6 1.2 1.3 1.9 2.5 2.5L7 6l2 2-1.2 1.5C4.5 9 1 5.5.5 2.2z"/></svg>02 7410 2200</div>
      <div class="contact-line"><svg class="icon" viewBox="0 0 10 10"><rect x="1" y="4" width="8" height="5" rx="1"/><rect x="3" y="1" width="4" height="3"/></svg>02 7410 2299</div>
    </div>
    <div class="salutation">Dear Martin</div>
    <div class="letter-body">
      <p>Sample text is used here to show the flow of a typical business letter on this page. It stands in for the real message and helps judge spacing, measure and overall balance. It has been set at the same size and weight as the final letter copy, so the page looks as it will once written. Placeholder lines like these have long served printers and designers as a way to preview a layout before the content arrives from the writer and editor.</p>
      <p>Sample text is used here to show the flow of a typical business letter on this page. It stands in for the real message and helps judge spacing, measure and overall balance of the sheet within the margins.</p>
      <p>Sample text is used here to show the flow of a typical business letter on this page. It stands in for the real message and helps judge spacing, measure and overall balance of the sheet within the margins. Sample text is used here to show the flow of a typical business letter on this page. It stands in for the real message and helps judge spacing, measure and overall balance of the sheet within the margins. Sample text is used here to show the flow of a typical business letter on this page. It stands in for the real message and helps judge spacing, measure and overall balance of the sheet within the margins.</p>
    </div>
    <div class="signoff">Very truly yours,</div>
    <div class="signature" role="img" aria-label="Handwritten signature of Martin Hale"></div>
    <div class="sign-title">CEO</div>
    <div class="map-fade" role="img" aria-label="Faint world map showing Asia and Australia"></div>
    <div class="footer-url">marwick.com.au</div>
  </section>

  <!-- Business card back -->
  <section class="sheet card-back" aria-label="Business card back">
    <div class="brand-name"><span class="word">Marwick</span><span class="line2">Global Logistics</span></div>
    <span class="brand-dot"></span>
    <div class="url">www.marwick.com.au</div>
  </section>

  <!-- Business card front -->
  <section class="sheet card-front" aria-label="Business card front">
    <div class="brand-name"><span class="word">Marwick</span><span class="line2">Global Logistics</span></div>
    <span class="brand-dot"></span>
    <div class="person"><div>Owen Carlisle</div><div class="role">Managing Director</div></div>
    <div class="address"><div>58 Harbour Lane</div><div>Pyrmont</div><div>NSW 2009</div></div>
    <div class="card-contacts">
      <div class="contact-line"><svg class="icon" viewBox="0 0 10 10"><path d="M2 1l2 2-1 1.5c.6 1.2 1.3 1.9 2.5 2.5L7 6l2 2-1.2 1.5C4.5 9 1 5.5.5 2.2z"/></svg>02 7410 2200</div>
      <div class="contact-line"><svg class="icon" viewBox="0 0 10 10"><rect x="3" y="0" width="4" height="10" rx="1"/></svg>0400517382</div>
      <div class="contact-line"><svg class="icon" viewBox="0 0 10 10"><rect x="1" y="4" width="8" height="5" rx="1"/><rect x="3" y="1" width="4" height="3"/></svg>02 7410 2299</div>
      <div class="contact-line"><svg class="icon" viewBox="0 0 10 10"><rect x="1" y="1" width="8" height="8" rx="1.5"/></svg>marwick</div>
      <div class="contact-line"><svg class="icon" viewBox="0 0 10 10"><rect x="0" y="2" width="10" height="6" rx="1"/></svg>tobias@marwick.com.au</div>
      <div class="contact-line"><svg class="icon" viewBox="0 0 10 10"><circle cx="5" cy="5" r="4.5"/></svg>marwick.com.au</div>
    </div>
  </section>

  <!-- Compliment slip -->
  <section class="sheet slip" aria-label="Compliment slip">
    <div class="brand-name"><span class="word">Marwick</span><span class="line2">Global Logistics</span></div>
    <span class="brand-dot"></span>
    <div class="address"><div>58 Harbour Lane</div><div>Pyrmont</div><div>NSW 2009</div></div>
    <div class="map-fade" role="img" aria-label="Faint world map showing Asia and Australia"></div>
    <div class="footer-url">marwick.com.au</div>
  </section>

  <!-- Envelope -->
  <section class="sheet envelope" aria-label="Envelope">
    <svg class="flap" width="388" height="60" viewBox="0 0 388 60" aria-hidden="true">
      <defs>
        <radialGradient id="flapGlow" cx="50%" cy="30%" r="60%">
          <stop offset="0" stop-color="#4a8ccb"/>
          <stop offset=".6" stop-color="#24508f"/>
          <stop offset="1" stop-color="#1d3f7c"/>
        </radialGradient>
      </defs>
      <path d="M0 0H388L380 20Q372 36 330 40L220 54Q194 58 168 54L58 40Q16 36 8 20Z" fill="url(#flapGlow)"/>
    </svg>
    <div class="brand-name"><span class="word">Marwick</span><span class="line2">Global Logistics</span></div>
  </section>

  <!-- Note pad -->
  <section class="sheet notepad" aria-label="Note pad">
    <div class="brand-name"><span class="word">Marwick</span><span class="line2">Global Logistics</span></div>
    <span class="brand-dot"></span>
    <div class="note-lines"><span></span><span></span><span></span><span></span><span></span><span></span><span></span><span></span><span></span><span></span><span></span></div>
    <div class="map-fade" role="img" aria-label="Faint world map showing Asia and Australia"></div>
    <div class="address">
      <div>58 Harbour Lane</div><div>Pyrmont</div><div>NSW 2009</div>
      <div class="contact-line"><svg class="icon" viewBox="0 0 10 10"><path d="M2 1l2 2-1 1.5c.6 1.2 1.3 1.9 2.5 2.5L7 6l2 2-1.2 1.5C4.5 9 1 5.5.5 2.2z"/></svg>02 7410 2200</div>
      <div class="contact-line"><svg class="icon" viewBox="0 0 10 10"><rect x="1" y="4" width="8" height="5" rx="1"/><rect x="3" y="1" width="4" height="3"/></svg>02 7410 2299</div>
    </div>
    <div class="footer-url">marwick.com.au</div>
  </section>

</main>
</body>
</html>
```